Marrowfield Biomedical Research Institute (MBRX) Web Design

MBRX is a non-profit organization focused on saving the lives of terminally ill patients by becoming the leaders in cutting-edge research, innovative technologies, utilizing national and international partnerships as well as the associated allopathic and naturopathic treatments necessary to do so.

Our primary focus is raising funds to support the research and acquisition of new technologies for life saving treatments which are NOT a one size fits all approach like conventional medicine but rather a marriage of the latest technologies used in combination with other new treatment possibilities for a successful end result.

Our domain is marrowfieldbrx.org

Logo files are attached.

Looking for something clean, light, healthy.

Target Market(s)

The site should look and feel towards research/scientific grant writing.
Medical professionals, Medical Scientists.

Industry/Entity Type

Medical And Science

Number of Pages Required

4 page

Requirements
Nice to have
• Here are examples of sites I like in the order of how much I like them.
• https://www.palvenhope.org/give.html
• https://www.thekqtf.org/donate-to-kqtf
• https://www.velmorecure.org/we-are-vci/join-the-cause
• https://www.tumarex.org/involved/donate.html
• https://give.dwkt.org/checkout/donation?eid=58217
• https://www.quillavent.org/how-you-can-help
• https://donate3.tumarex.org/

```html
<!DOCTYPE html>
<html lang="en">
<head>
<meta charset="utf-8">
<title>Marrowfield Biomedical Research Institute</title>
<link href="https://fonts.googleapis.com/css2?family=Roboto:wght@400;500;700&display=swap" rel="stylesheet">
<style>
:root{
  --blue:#1b73bd;
  --blue-dark:#1766a8;
  --footer-blue:#1f6db3;
  --green:#4a8b3a;
  --green-dark:#3e7a30;
  --ink:#222;
  --muted:#444;
  --light:#efefef;
  --topbar:#3a3a3a;
  --white:#fff;
}
*{box-sizing:border-box;margin:0;padding:0}
html,body{width:1200px;height:3965px;overflow:hidden}
body{font-family:"Roboto",Arial,sans-serif;color:var(--ink);background:var(--white);position:relative}
.abs{position:absolute}
.btn{position:absolute;display:flex;align-items:center;justify-content:center;background:var(--green);color:var(--white);font-weight:700;font-size:14px;border-radius:4px;box-shadow:0 2px 0 var(--green-dark)}
.center{text-align:center;left:0;width:1200px}
.sec-title{position:absolute;font-size:28px;font-weight:500;color:var(--ink);letter-spacing:.5px}
.sec-sub{position:absolute;font-size:13px;color:var(--muted)}

/* top bar */
.topbar{position:absolute;top:0;left:0;width:1200px;height:42px;background:var(--topbar);color:var(--white);font-size:13px;font-weight:500}
.social{position:absolute;display:flex;gap:14px}
.social span{width:13px;height:13px;border-radius:50%;background:currentColor;display:block}

/* header */
.header{position:absolute;top:42px;left:0;width:1200px;height:116px;background:var(--white)}
.brand{position:absolute;left:119px;top:28px;display:flex;align-items:center;gap:10px}
.brand-mark{width:44px;height:44px;border-radius:50%;background:var(--green)}
.brand-name{font-size:16px;font-weight:700;color:var(--blue);line-height:1.15;width:170px}
.nav{position:absolute;left:560px;top:52px;display:flex;gap:24px;font-size:13px;font-weight:500;color:#333;letter-spacing:.5px}
.donate-top{position:absolute;left:975px;top:50px;width:108px;height:27px;background:var(--blue);color:var(--white);font-size:13px;font-weight:700;display:flex;align-items:center;justify-content:center;border-radius:3px}

/* hero */
.hero{position:absolute;top:158px;left:0;width:1200px;height:608px;background:linear-gradient(90deg,#3f5262 0%,#6f8391 35%,#8fa2ae 55%,#5e7383 100%)}
.hero-title{position:absolute;top:436px;font-size:30px;font-weight:700;color:var(--white);letter-spacing:1px}
.hero-sub{position:absolute;top:478px;font-size:13px;font-weight:700;color:var(--white);line-height:18px}
.arrow{position:absolute;top:438px;width:20px;height:34px}
.dots{position:absolute;top:582px;left:576px;display:flex;gap:6px}
.dots span{width:9px;height:9px;border-radius:50%;background:var(--white)}
.dots span:first-child{background:none;border:2px solid var(--white)}
.grayband{position:absolute;top:766px;left:0;width:1200px;height:177px;background:var(--light)}
.card{position:absolute;top:660px;width:238px;height:226px}
.card-head{height:102px;background:var(--blue);color:var(--white);text-align:center;padding-top:16px}
.card-head h3{font-size:18px;font-weight:700;margin-bottom:10px}
.card-head p{font-size:12px;font-weight:700;line-height:15px;padding:0 18px}
.card-img{height:124px}

/* services */
.molecule{position:absolute;left:450px;top:1170px;width:240px;height:210px;border-radius:8px;background:radial-gradient(circle at 50% 50%,#d6e7f5 0%,#eef5fb 70%,#ffffff 100%)}
.svc-label{position:absolute;font-size:12px;color:#333;line-height:15px}
.svc-label h4{font-size:17px;font-weight:400;color:#222;margin-bottom:6px;display:flex;align-items:center;gap:8px}
.svc-label h4 i{width:20px;height:20px;border-radius:50%;background:var(--blue);display:inline-block}
.more-dot{display:inline-block;width:8px;height:8px;border-radius:50%;background:#7fb1dd;margin-left:4px}

/* donate banner */
.banner{position:absolute;top:1657px;left:0;width:1200px;height:386px;background:linear-gradient(90deg,#3d5668 0%,#7c93a6 40%,#9aa8b4 60%,#4f6270 100%)}
.banner-text{position:absolute;right:164px;text-align:right;color:var(--white)}
.banner-text h2{font-size:22px;font-weight:700;line-height:29px}
.banner-text p{font-size:13px;font-weight:700;line-height:17px;margin-top:12px;width:290px;margin-left:auto}

/* testimonials */
.patients{position:absolute;top:2043px;left:0;width:1200px;height:592px;background:var(--light)}
.oct{position:absolute;clip-path:polygon(30% 0,70% 0,100% 30%,100% 70%,70% 100%,30% 100%,0 70%,0 30%)}
.quote-mark{position:absolute;font-size:40px;font-weight:700;color:var(--blue);line-height:1}

/* blog */
.post{position:absolute;top:2788px;width:304px}
.post-img{height:238px;border-radius:4px}
.post-meta{display:flex;gap:10px;margin-top:21px}
.date{width:40px;height:40px;background:var(--blue);color:var(--white);text-align:center;font-size:14px;font-weight:700;line-height:16px;padding-top:5px}
.date small{display:block;font-size:9px;font-weight:400}
.post-meta h4{font-size:14px;font-weight:500;color:#222}
.post-meta span{font-size:11px;color:#444}
.post p{font-size:13px;line-height:16px;color:#333;margin-top:16px}
.read{font-size:13px;color:#222;margin-top:4px;display:block}

/* newsletter */
.newsletter{position:absolute;top:3325px;left:0;width:1200px;height:270px;background:var(--light)}
.field{position:absolute;background:var(--white);border:1px solid #ddd;font-size:12px;color:#888;padding:11px 14px}

/* footer */
.footer{position:absolute;top:3595px;left:0;width:1200px;height:303px;background:var(--footer-blue);color:var(--white)}
.footer h5{font-size:13px;font-weight:700;letter-spacing:.5px}
.footer .small{font-size:12px;line-height:19px}
.ffield{position:absolute;background:var(--blue-dark);border:1px solid #3b86c6;font-size:11px;color:#dfe9f4;padding:6px 8px}
.bottombar{position:absolute;top:3898px;left:0;width:1200px;height:67px;background:var(--white)}
</style>
</head>
<body>

<div class="topbar">
  <span class="abs" style="left:119px;top:12px">+ 555 014 7292</span>
  <span class="abs" style="left:537px;top:12px">info@marrowfieldbrx.org</span>
  <div class="social" style="left:957px;top:14px;color:#fff"><span></span><span></span><span></span><span></span><span></span></div>
</div>

<header class="header">
  <div class="brand"><div class="brand-mark"></div><div class="brand-name">Marrowfield Biomedical Research Institute</div></div>
  <nav class="nav"><span>ABOUT US</span><span>SERVICES</span><span>PATIENTS</span><span>BLOG</span></nav>
  <svg class="abs" style="left:932px;top:55px" width="14" height="14" viewBox="0 0 14 14"><circle cx="5.5" cy="5.5" r="4.2" fill="none" stroke="#333" stroke-width="2"/><line x1="8.6" y1="8.6" x2="13" y2="13" stroke="#333" stroke-width="2"/></svg>
  <a class="donate-top">DONATE</a>
</header>

<section class="hero" role="img" aria-label="Scientists in masks and lab coats working with test tubes in a laboratory"></section>
<div class="hero-title center">INNOVATION ADVANCE MEDICIANES</div>
<div class="hero-sub center">Lorem Ipsum is simply dummy text of the printing and industry.<br>Lorem Ipsum has been the industry's</div>
<a class="btn" style="left:520px;top:531px;width:162px;height:38px">Donate Now</a>
<svg class="arrow" style="left:50px" viewBox="0 0 20 34"><polyline points="16,3 4,17 16,31" fill="none" stroke="#fff" stroke-width="4"/></svg>
<svg class="arrow" style="left:1132px" viewBox="0 0 20 34"><polyline points="4,3 16,17 4,31" fill="none" stroke="#fff" stroke-width="4"/></svg>
<div class="dots"><span></span><span></span><span></span></div>

<div class="grayband"></div>
<div class="card" style="left:211px"><div class="card-head"><h3>Ways to Donate</h3><p>Lorem Ipsum is simply dummy text of the printing</p></div><div class="card-img" role="img" aria-label="Blue molecular model" style="background:linear-gradient(135deg,#bcd9ee,#5c9fd0)"></div></div>
<div class="card" style="left:478px"><div class="card-head"><h3>Why Donate?</h3><p>Lorem Ipsum is simply dummy text of the printing</p></div><div class="card-img" role="img" aria-label="Hands holding colourful pills" style="background:linear-gradient(135deg,#e8c7ac,#8fa7bd)"></div></div>
<div class="card" style="left:742px"><div class="card-head"><h3>Donation FAQs</h3><p>Lorem Ipsum is simply dummy text of the printing</p></div><div class="card-img" role="img" aria-label="Fingers holding a capsule" style="background:linear-gradient(135deg,#e5c9b4,#b88d70)"></div></div>

<h2 class="sec-title center" style="top:984px">Our Services</h2>
<p class="sec-sub center" style="top:1020px">Lorem Ipsum is simply dummy text of the printing and industry.</p>

<div class="molecule" role="img" aria-label="Blue molecule structure illustration linking the four services"></div>
<div class="svc-label" style="left:412px;top:1090px;width:200px"><h4 style="margin-left:56px">Medical Care <i></i></h4>Lorem Ipsum is simply dummy text the printing and industry. Lorem Ipsum..<span class="more-dot"></span></div>
<div class="svc-label" style="left:228px;top:1214px;width:210px;text-align:right"><h4 style="justify-content:flex-end;margin-right:20px">Research <i></i></h4>Lorem Ipsum is simply dummy text the printing and industry Lorem Ipsum..<span class="more-dot"></span></div>
<div class="svc-label" style="left:742px;top:1300px;width:210px"><h4 style="margin-left:10px"><i></i> Allopathic</h4>Lorem Ipsum is simply dummy text the printing and industry. Lorem Ipsum..<span class="more-dot"></span></div>
<div class="svc-label" style="left:540px;top:1422px;width:210px"><h4><i></i> Naturopathic</h4>Lorem Ipsum is simply dummy text the printing and industry. Lorem Ipsum..<span class="more-dot"></span></div>
<a class="btn" style="left:539px;top:1556px;width:156px;height:38px">View All Services</a>

<section class="banner" role="img" aria-label="Gloved hands holding a petri dish in a laboratory, with a white DNA strand decoration on the left"></section>
<div class="banner-text" style="top:1766px">
  <h2>Donate to the<br>Innovation Advance Medicianes</h2>
  <p>Lorem Ipsum is simply dummy text of the printing Lorem Ipsum has been the industry's</p>
</div>
<a class="btn" style="left:885px;top:1903px;width:159px;height:38px">Read More</a>

<section class="patients">
  <h2 class="sec-title center" style="top:68px">Patient Says</h2>
  <p class="sec-sub center" style="top:104px">Lorem Ipsum is simply dummy text of the printing and industry.</p>
  <svg class="abs" style="left:320px;top:240px" width="12" height="18" viewBox="0 0 12 18"><polyline points="10,2 3,9 10,16" fill="none" stroke="#555" stroke-width="2"/></svg>
  <svg class="abs" style="left:870px;top:240px" width="12" height="18" viewBox="0 0 12 18"><polyline points="2,2 9,9 2,16" fill="none" stroke="#555" stroke-width="2"/></svg>
  <div class="oct" style="left:372px;top:187px;width:122px;height:122px;background:linear-gradient(160deg,#c8a48a,#7f6a5e)" role="img" aria-label="Portrait of a smiling patient"></div>
  <div class="oct" style="left:510px;top:156px;width:185px;height:185px;background:linear-gradient(160deg,#d3b7a2,#8c7b70)" role="img" aria-label="Portrait of a patient at a desk"></div>
  <div class="oct" style="left:711px;top:187px;width:122px;height:122px;background:linear-gradient(160deg,#e0cdb8,#9aa9b8)" role="img" aria-label="Portrait of a patient in a clinic"></div>
  <p class="center abs" style="top:351px;font-size:15px;font-weight:700;color:var(--blue)">DANIEL HART</p>
  <p class="center abs" style="top:378px;font-size:13px;color:#333">Creative Director</p>
  <p class="abs" style="left:336px;top:398px;width:544px;text-align:center;font-size:13px;line-height:17px;color:#333">Lorem Ipsum is simply dummy text of the printing and typesetting industry. Lorem Ipsum has been the industry's standard dummy text ever since the 1500s, when an unknown printer took a galley of type and scrambled</p>
  <span class="quote-mark" style="left:296px;top:366px">&ldquo;</span>
  <span class="quote-mark" style="left:836px;top:440px">&rdquo;</span>
  <a class="btn" style="left:526px;top:515px;width:159px;height:38px">View More</a>
</section>

<h2 class="sec-title center" style="top:2692px">Our Blog</h2>
<p class="sec-sub center" style="top:2729px">Lorem Ipsum is simply dummy text of the printing and industry.</p>
<article class="post" style="left:119px"><div class="post-img" role="img" aria-label="Stethoscope with a molecule model" style="background:linear-gradient(135deg,#d7e9f6,#4f95cc)"></div><div class="post-meta"><div class="date">22<small>Nov</small></div><div><h4>Benefits of Medical Science</h4><span>Article shared by Alan Reed</span></div></div><p>Lorem Ipsum is simply dummy text of the printing and typesetting industry. Lorem Ipsum has been the industry's standard dummy text ever since the 1500s.</p><span class="read">Read More..<span class="more-dot"></span></span></article>
<article class="post" style="left:447px"><div class="post-img" role="img" aria-label="Gloved hand with coloured flasks in a lab" style="background:linear-gradient(135deg,#cfe0f0,#6d8fbf)"></div><div class="post-meta"><div class="date">22<small>Nov</small></div><div><h4>Benefits of Medical Science</h4><span>Article shared by Alan Reed</span></div></div><p>Lorem Ipsum is simply dummy text of the printing and typesetting industry. Lorem Ipsum has been the industry's standard dummy text ever since the 1500s.</p><span class="read">Read More..<span class="more-dot"></span></span></article>
<article class="post" style="left:774px"><div class="post-img" role="img" aria-label="Two researchers examining a petri dish" style="background:linear-gradient(135deg,#e9eef3,#9fb4c6)"></div><div class="post-meta"><div class="date">22<small>Nov</small></div><div><h4>Benefits of Medical Science</h4><span>Article shared by Alan Reed</span></div></div><p>Lorem Ipsum is simply dummy text of the printing and typesetting industry. Lorem Ipsum has been the industry's standard dummy text ever since the 1500s.</p><span class="read">Read More..<span class="more-dot"></span></span></article>
<a class="btn" style="left:526px;top:3230px;width:159px;height:38px">View More</a>

<section class="newsletter">
  <h2 class="center abs" style="top:70px;font-size:23px;font-weight:500;letter-spacing:1px">SUBSCRIBE TO OUR NEWSLETTER</h2>
  <p class="center abs" style="top:100px;font-size:14px;font-weight:700;letter-spacing:.5px;color:#333">TO RECEIVE THE LATEST NEWS AND UPDATE</p>
  <div class="field" style="left:304px;top:150px;width:428px;height:38px">Your E-Mail</div>
  <a class="btn" style="left:732px;top:150px;width:130px;height:38px;border-radius:0 4px 4px 0">SUBMIT</a>
</section>

<footer class="footer">
  <div class="abs" style="left:119px;top:50px;display:flex;align-items:center;gap:8px"><div style="width:22px;height:22px;border-radius:50%;background:#fff"></div><span style="font-size:18px;font-weight:700">MBRX</span></div>
  <p class="abs small" style="left:119px;top:110px;width:200px;font-weight:700">Lorem Ipsum is simply dummy text of the printing and typesetting industry. Lorem Ipsum</p>
  <p class="abs small" style="left:119px;top:172px">Read More.. <span class="more-dot"></span></p>
  <div class="abs" style="left:365px;top:72px"><h5>QUICK LINK</h5><p class="small" style="margin-top:12px;font-weight:500">About us<br>Services<br>Patients<br>Blog</p></div>
  <div class="abs" style="left:510px;top:72px"><h5>CONTACT US</h5><p class="small" style="margin-top:12px;font-weight:500">Address&nbsp;:&nbsp; 123th Street, City<br>Phone&nbsp;&nbsp;&nbsp;:&nbsp; +1 555 014 7290<br>Fax&nbsp;&nbsp;&nbsp;&nbsp;&nbsp;&nbsp;&nbsp;&nbsp;:&nbsp; +1 555 014 7291<br>E-mail&nbsp;&nbsp;&nbsp;:&nbsp; info@mbrx.org</p></div>
  <h5 class="abs" style="left:764px;top:72px">QUICK CONTACT</h5>
  <div class="ffield" style="left:764px;top:121px;width:136px;height:27px">Name</div>
  <div class="ffield" style="left:903px;top:121px;width:136px;height:27px">Phone</div>
  <div class="ffield" style="left:764px;top:158px;width:275px;height:58px">Message</div>
  <a class="btn" style="left:904px;top:229px;width:135px;height:38px;font-size:12px">SEND</a>
</footer>

<div class="bottombar">
  <p class="abs" style="left:119px;top:22px;font-size:13px;color:#333">Privacy policy · Legal Mentions · Terms and Conditions</p>
  <div class="social" style="left:856px;top:25px;gap:33px;color:#333"><span></span><span></span><span></span><span></span><span></span></div>
</div>

</body>
</html>
```